Roadside building business signage for a holistic health clinic.

Replace signs as shown in the attached file. They are perforated stickers that go on the windows as shown. Looking for something that has our logo and says the name of the practice with logo (Fernbrook Health & Wellness) also boldly says Acupuncture, IV Vitamins, and Holistic Health.
Possibly our phone number as well 318-627-5194
Updates

Please don't use pink except the logo. Earthy, organic tone colors appreciated.

Need of eye catching window signage of a holistic clinic on a brick building. Pink, purple, sage green, white color. Logo is pink on a white background. Please don't overload with too much pink. Words to include are "Fernbrook Health and Wellness(name of business)", "Direct Primary Care", " Medical acupuncture", "IV Vitamin Therapy", "fernbrookcare-example.com","318-627-5194".

Target Market(s)

People will see in their cars passing by the building. Busy roadside so need to be visible while passing in fast speed.

Industry/Entity Type

Health & Wellness

Font styles to use
Sans Serif

Colors

Designer to choose colors to be used in the design.

Requirements
Must have
• On sign must have words Holistic Medicine, Medical Acupuncture, Direct Primary Care and IV vitamins.
Nice to have
• Simple, minimalistic, artistic yet has clear message. White, Black, Violet, Pink (logo), Dark green, Sage green.
Should not have
• Bold colors (red, yellow, blue), same tone colors. Blue waves on the current signage (uploaded file) must go.

```html
<!DOCTYPE html>
<html lang="en">
<head>
<meta charset="utf-8">
<title>Fernbrook Health &amp; Wellness — Window Signage</title>
<link rel="stylesheet" href="https://fonts.googleapis.com/css2?family=Nunito+Sans:wght@500;800&display=swap">
<style>
  :root {
    --backdrop: #ece9e6;
    --sage: #7f8473;
    --sage-deep: #737866;
    --panel: #f1fbe6;
    --forest: #1d5842;
    --service-text: #7a7f6d;
    --blossom: #e0408e;
    --shadow: 3px 4px 6px rgba(0, 0, 0, 0.28);
  }
  * { margin: 0; padding: 0; box-sizing: border-box; }
  html, body { width: 769px; height: 1200px; overflow: hidden; background: var(--backdrop); }
  body { position: relative; font-family: "Nunito Sans", sans-serif; }

  .tile {
    position: absolute;
    box-shadow: var(--shadow);
  }
  .tile--pattern {
    background: linear-gradient(160deg, var(--sage) 0%, var(--sage-deep) 100%);
  }
  .tile--arch-right { border-top-right-radius: 100%; }
  .tile--arch-left { border-top-left-radius: 100%; }
  .tile--panel { background: var(--panel); }

  .brand {
    display: flex;
    flex-direction: column;
    align-items: center;
    justify-content: center;
    height: 100%;
    color: var(--forest);
    font-weight: 800;
    text-align: center;
  }
  .brand__mark {
    width: 30px; height: 30px;
    border-radius: 50%;
    background: var(--blossom);
    margin-bottom: 10px;
  }
  .brand__name { font-size: 21px; letter-spacing: 1.5px; line-height: 1.05; text-transform: uppercase; }
  .brand__tagline { font-size: 7px; letter-spacing: 1.6px; text-transform: uppercase; margin-top: 3px; }

  .services {
    padding: 13px 0 0 13px;
    color: var(--service-text);
  }
  .services__list {
    list-style: none;
    font-weight: 800;
    font-size: 16.2px;
    line-height: 1.36;
  }
  .services__phone {
    font-weight: 500;
    font-size: 15px;
    margin-top: 10px;
    letter-spacing: 0.3px;
  }
</style>
</head>
<body>

  <!-- Single window set -->
  <div class="tile tile--pattern tile--arch-right" style="left:234px; top:54px; width:155px; height:164px;" role="img" aria-label="Sage green panel with flowing organic stripe pattern"></div>

  <div class="tile tile--panel" style="left:234px; top:227px; width:155px; height:162px;">
    <div class="brand">
      <span class="brand__mark"></span>
      <span class="brand__name">Fernbrook</span>
      <span class="brand__tagline">Health &amp; Wellness</span>
    </div>
  </div>

  <div class="tile tile--panel services" style="left:400px; top:227px; width:154px; height:162px;">
    <ul class="services__list">
      <li>Acupuncture,</li>
      <li>IV Vitamins,</li>
      <li>Primary care,</li>
      <li>and</li>
      <li>Holistic Health.</li>
    </ul>
    <p class="services__phone">318-627-5194</p>
  </div>

  <div class="tile tile--pattern" style="left:234px; top:398px; width:155px; height:161px;" role="img" aria-label="Sage green panel with vertical organic stripe pattern"></div>
  <div class="tile tile--pattern" style="left:400px; top:398px; width:154px; height:161px;" role="img" aria-label="Sage green panel with vertical organic stripe pattern"></div>

  <!-- Double window set -->
  <div class="tile tile--pattern tile--arch-left" style="left:236px; top:644px; width:149px; height:155px;" role="img" aria-label="Sage green arch half with flowing organic stripe pattern"></div>
  <div class="tile tile--pattern tile--arch-right" style="left:392px; top:644px; width:149px; height:155px;" role="img" aria-label="Sage green arch half with flowing organic stripe pattern"></div>

  <div class="tile tile--panel" style="left:79px; top:807px; width:148px; height:155px;">
    <div class="brand">
      <span class="brand__mark"></span>
      <span class="brand__name">Fernbrook</span>
      <span class="brand__tagline">Health &amp; Wellness</span>
    </div>
  </div>

  <div class="tile tile--panel services" style="left:236px; top:807px; width:148px; height:155px;">
    <ul class="services__list">
      <li>Acupuncture,</li>
      <li>IV Vitamins,</li>
      <li>Primary care,</li>
      <li>and</li>
      <li>Holistic Health.</li>
    </ul>
    <p class="services__phone">318-627-5194</p>
  </div>

  <div class="tile tile--panel" style="left:392px; top:807px; width:148px; height:155px;">
    <div class="brand">
      <span class="brand__mark"></span>
      <span class="brand__name">Fernbrook</span>
      <span class="brand__tagline">Health &amp; Wellness</span>
    </div>
  </div>

  <div class="tile tile--panel services" style="left:549px; top:807px; width:148px; height:155px;">
    <ul class="services__list">
      <li>Acupuncture,</li>
      <li>IV Vitamins,</li>
      <li>Primary care,</li>
      <li>and</li>
      <li>Holistic Health.</li>
    </ul>
    <p class="services__phone">318-627-5194</p>
  </div>

  <div class="tile tile--pattern" style="left:79px; top:971px; width:148px; height:154px;" role="img" aria-label="Sage green panel with vertical organic stripe pattern"></div>
  <div class="tile tile--pattern" style="left:236px; top:971px; width:148px; height:154px;" role="img" aria-label="Sage green panel with vertical organic stripe pattern"></div>
  <div class="tile tile--pattern" style="left:392px; top:971px; width:148px; height:154px;" role="img" aria-label="Sage green panel with vertical organic stripe pattern"></div>
  <div class="tile tile--pattern" style="left:549px; top:971px; width:148px; height:154px;" role="img" aria-label="Sage green panel with vertical organic stripe pattern"></div>

</body>
</html>
```